Bus Card for Organic Hydroponic Produce company

We need a business card for a budding new business. We grow 100% organic, 100% hydroponic, 100% GMO free produce for sale in our local area. We need something bold and dynamic, not simple and elegant. We want to catch peoples attention and get them to visit our website to view more information about our products and services. Its difficult to explain on a business card the differences between our produce (tomatoes, cucumbers, peppers, etc...) and the kind they would buy at the local grocer or market. , so we need to push them to the website.
We have been brainstorming names for the company and have a few in mind, so choose whichever speaks most to your artistic flair and propose a card based on that one, or both. #1 "Marrowfield Organics" with a slogan something like....." When merely growing green merely isn't quite enough" OR #2 "Quillbrook Organics" with a slogan similar to...."The cutting edge in cleaner, purer organics" OR #3" "Tandrel Organics" with a slogan similar to: "Building a healthier future for those we leave behind"" OR #4 "Loamwise Path" with a slogan similar to: "Purity by Simplicity"
Eventually we will need assistance with web design, promotional and sales materials, etc. so if you offer those services, please indicate that with the design, though it is NOT necessary to offer any additional services to win this contest. WE will pick the winner solely on the business card we like the most.
We want something that stands out, and especially with the name "Oda's organics", we understand that a creative mind may wander into certain attention getting means that may not be quite within the realm of what we can hand out at our local grocer or farmers market. We definitely are not opposed to a little salacious undertone or allusion to attract attention, but please keep it tasteful if you skirt that grey area.
For our card, we use an online printer that can add foils, special die cuts, double sided cards, 3-d cards (we love these 32 pt cards), transparent or translucent cards and more. We love cards that have some of these things where possible and on all of our other business' cards we get rave reviews from customers about their uniqueness. plumtessa.com has the info on these accents if you wish to view what I am referencing.
So in conclusion, we want a unique, stylish, bold, vivid, 2 sided business card that will really stand out. Just usw a generic phone number and website for now and we will add them as they become available. Please email with any questions! Thanks in advance for your effort and creativity!
Target Market(s)
We are targeting parents who are conceintous of what their children and families are eating. Our target audience are moms, but we don't want to exclude anyone else who chooses to eat more healthy. Our target customer is the same customer that would shop at Brightcart stores or local farmers markets

```html
<!DOCTYPE html>
<html lang="en">
<head>
<meta charset="utf-8">
<title>Quillbrook Organics – Business Card</title>
<link rel="stylesheet" href="https://fonts.googleapis.com/css2?family=Exo+2:wght@500;600;800&display=swap">
<style>
  :root {
    --canvas: #efece6;
    --green-deep: #0c7a34;
    --green-mid: #159a3c;
    --green-light: #2aa84a;
    --green-soft: #47b657;
    --lime: #c6e61c;
    --lime-dark: #9fcb1a;
    --white: #ffffff;
    --card-shadow: rgba(20, 50, 25, 0.25);
  }
  * { box-sizing: border-box; margin: 0; padding: 0; }
  html, body {
    width: 1200px; height: 1023px; overflow: hidden;
    background: var(--canvas);
    font-family: "Exo 2", "Trebuchet MS", sans-serif;
  }
  .stage { position: relative; width: 1200px; height: 1023px; }
  .card {
    position: absolute; top: 196px;
    width: 360px; height: 630px;
    border-radius: 0 64px 0 64px;
    overflow: hidden;
    box-shadow: 0 14px 30px var(--card-shadow);
  }

  /* Front */
  .card-front {
    left: 190px;
    background: linear-gradient(180deg, var(--green-mid) 0%, var(--green-deep) 100%);
  }
  .front-head { position: absolute; top: 40px; left: 30px; right: 24px; }
  .brand-name {
    display: flex; align-items: flex-end; gap: 8px;
    color: var(--lime); font-weight: 800;
    font-size: 46px; line-height: 0.95; letter-spacing: -0.5px;
  }
  .brand-dot {
    width: 14px; height: 14px; border-radius: 50%;
    background: var(--lime); flex: none; margin-bottom: 8px;
  }
  .tagline {
    margin-top: 16px; color: var(--white);
    font-weight: 500; font-size: 19px; line-height: 1.2;
  }
  .front-lower { position: absolute; left: 0; right: 0; top: 238px; bottom: 0; }
  .front-lower svg { position: absolute; inset: 0; width: 100%; height: 100%; }
  .contact {
    position: absolute; left: 30px; top: 300px;
    color: var(--white); font-weight: 500;
  }
  .contact-name { font-size: 17px; font-weight: 600; margin-bottom: 18px; }
  .contact-list { list-style: none; }
  .contact-list li {
    display: flex; align-items: center; gap: 10px;
    font-size: 17px; line-height: 1.4;
  }
  .contact-list .no-icon { padding-left: 24px; }
  .icon { width: 14px; height: 14px; flex: none; }

  /* Back */
  .card-back { left: 650px; }
  .produce-pattern {
    position: absolute; inset: 0;
    background: radial-gradient(circle at 40% 35%, var(--green-soft) 0%, var(--green-light) 35%, var(--green-mid) 70%, var(--green-deep) 100%);
  }
  .back-brand {
    position: absolute; left: 50%; top: 50%;
    transform: translate(-50%, -50%) rotate(90deg);
    display: flex; align-items: flex-end; gap: 10px;
    color: var(--lime); font-weight: 800;
    font-size: 62px; line-height: 0.95; white-space: nowrap;
  }
  .back-brand .brand-dot { width: 18px; height: 18px; margin-bottom: 11px; }
</style>
</head>
<body>
<main class="stage">
  <section class="card card-front" aria-label="Card front">
    <header class="front-head">
      <h1 class="brand-name"><span>Quillbrook<br>Organics</span><span class="brand-dot"></span></h1>
      <p class="tagline">The cutting edge in cleaner,<br>purer organics</p>
    </header>
    <div class="front-lower">
      <svg viewBox="0 0 360 392" preserveAspectRatio="none" aria-hidden="true">
        <defs>
          <linearGradient id="lowerFill" x1="0" y1="0" x2="0" y2="1">
            <stop offset="0" stop-color="#2aa84a"/>
            <stop offset="1" stop-color="#159a3c"/>
          </linearGradient>
        </defs>
        <path d="M0 30 Q180 -6 360 86 L360 392 L0 392 Z" fill="url(#lowerFill)"/>
        <path d="M0 22 Q180 -16 360 76 L360 92 Q180 0 0 36 Z" fill="var(--lime)"/>
        <path d="M0 36 Q180 0 360 92 L360 98 Q180 8 0 42 Z" fill="var(--lime-dark)"/>
      </svg>
    </div>
    <div class="contact">
      <p class="contact-name">Your Name</p>
      <ul class="contact-list">
        <li>
          <svg class="icon" viewBox="0 0 14 14"><rect x="3" y="1" width="8" height="12" rx="1.5" fill="none" stroke="var(--lime)" stroke-width="1.5"/></svg>
          555-555-5555
        </li>
        <li>
          <svg class="icon" viewBox="0 0 14 14"><rect x="1" y="3" width="12" height="8" fill="none" stroke="var(--lime)" stroke-width="1.5"/><path d="M1 3 L7 8 L13 3" fill="none" stroke="var(--lime)" stroke-width="1.5"/></svg>
          Odasorganics@mailvane.com
        </li>
        <li>
          <svg class="icon" viewBox="0 0 14 14"><circle cx="7" cy="7" r="5.5" fill="none" stroke="var(--lime)" stroke-width="1.5"/><path d="M1.5 7 H12.5 M7 1.5 Q3.5 7 7 12.5 M7 1.5 Q10.5 7 7 12.5" fill="none" stroke="var(--lime)" stroke-width="1.2"/></svg>
          www.OdasOrganics.com
        </li>
        <li>
          <svg class="icon" viewBox="0 0 14 14"><path d="M7 13 C3 8 2.5 6.5 2.5 5 A4.5 4.5 0 0 1 11.5 5 C11.5 6.5 11 8 7 13 Z" fill="var(--lime)"/><circle cx="7" cy="5" r="1.6" fill="var(--green-mid)"/></svg>
          48 Fernhollow Lane,
        </li>
        <li class="no-icon">Harrowby Bay, ZT 10482</li>
      </ul>
    </div>
  </section>

  <section class="card card-back" aria-label="Card back">
    <div class="produce-pattern" role="img" aria-label="Tone-on-tone green pattern of fruit and vegetables: grapes, banana, citrus slice, watermelon wedge, strawberry, apples and leaves"></div>
    <p class="back-brand"><span>Quillbrook<br>Organics</span><span class="brand-dot"></span></p>
  </section>
</main>
</body>
</html>
```